The Pane Masters- we supply and install new windows for customers homes

We require a 12 page brochure (8 pages with a cover) This is to be finished 8.5 x 11 with the layout to be 17.25" x 11.25" (full bleed). These pages will be folded and saddlestitched to the finished size. We require our designer to be familiar with print layouts. I have attached a flow sheet in word that describes the content of each page. Additionally I have picture files co-ordinated to each page. Please provide a sample layout of any page for review and selection. Our colour themes as indicated in our logo are CMYK 0 80 100 0 and CMYK 65 58 58 38. We have no concept as to design but it must look professional. Upon successful selection all of the files would be made available

```html
<!DOCTYPE html>
<html lang="en">
<head>
<meta charset="utf-8">
<title>The Pane Masters – Product Catalog 2019</title>
<link rel="stylesheet" href="https://fonts.googleapis.com/css2?family=Audiowide&family=Arimo:wght@400&display=swap">
<style>
  :root {
    --brand-orange: #f15a22;
    --brand-grey: #4b4b4b;
    --ink: #111111;
    --paper: #ffffff;
    --seal-grey: #d9dce1;
    --sky-top: #1f4f9c;
    --sky-mid: #3f5f8f;
    --house-warm: #8c8068;
    --lawn-dark: #27311f;
  }
  html, body {
    margin: 0;
    padding: 0;
    width: 1200px;
    height: 824px;
    overflow: hidden;
    background: var(--paper);
  }
  .spread {
    position: relative;
    width: 1200px;
    height: 824px;
    background: var(--paper);
    overflow: hidden;
  }
  .spread-art {
    position: absolute;
    inset: 0;
  }
  .membership-seal {
    position: absolute;
    left: 64px;
    top: 180px;
    width: 84px;
    height: 84px;
    border-radius: 50%;
    background: var(--seal-grey);
  }
  .contact-block {
    position: absolute;
    left: 48px;
    bottom: 44px;
    margin: 0;
    font-family: "Arimo", Arial, sans-serif;
    font-size: 15px;
    line-height: 1.3;
    color: var(--paper);
    font-style: normal;
  }
  .brand-name {
    position: absolute;
    left: 648px;
    top: 78px;
    display: flex;
    align-items: center;
    gap: 10px;
    font-family: "Audiowide", sans-serif;
    font-size: 20px;
    color: var(--brand-orange);
    letter-spacing: 1px;
  }
  .brand-name .mark {
    width: 18px;
    height: 18px;
    background: var(--brand-orange);
  }
  .catalog-title {
    position: absolute;
    right: 60px;
    top: 600px;
    margin: 0;
    font-family: "Audiowide", sans-serif;
    font-weight: 400;
    text-align: right;
    line-height: 1;
  }
  .catalog-title .line-product {
    display: block;
    font-size: 44px;
    color: var(--brand-orange);
  }
  .catalog-title .line-catalog {
    display: block;
    font-size: 44px;
    color: var(--ink);
    margin-top: 4px;
  }
  .catalog-title .line-year {
    display: block;
    font-size: 16px;
    color: var(--ink);
    margin-top: 4px;
  }
</style>
</head>
<body>
<main class="spread">
  <svg class="spread-art" width="1200" height="824" viewBox="0 0 1200 824">
    <defs>
      <linearGradient id="photoTones" x1="0" y1="0" x2="0" y2="1">
        <stop offset="0" stop-color="#1f4f9c"/>
        <stop offset="0.35" stop-color="#3f5f8f"/>
        <stop offset="0.6" stop-color="#8c8068"/>
        <stop offset="1" stop-color="#27311f"/>
      </linearGradient>
    </defs>
    <path class="cover-photo" role="img"
          aria-label="Photograph of a large two-storey home with a wraparound porch, lit windows and soffit lights at dusk"
          d="M0,360 C150,240 360,170 600,190 C720,200 800,140 830,0 L1200,0 L1200,300 C1150,450 1050,520 900,540 C750,560 650,560 600,600 C480,650 420,720 410,824 L0,824 Z"
          fill="url(#photoTones)"/>
    <g class="accent-curves" fill="none" stroke="#f15a22" stroke-width="4">
      <path d="M0,360 C150,240 360,170 600,190 C720,200 800,140 830,0"/>
      <path d="M1200,300 C1150,450 1050,520 900,540 C750,560 650,560 600,600 C480,650 420,720 410,824"/>
    </g>
  </svg>

  <div class="membership-seal" aria-hidden="true"></div>

  <address class="contact-block">
    The Pane Masters Ltd.<br>
    410, 2275 Harlow Ridge Road NW<br>
    Calgary AB T3K 1P8<br>
    403.555.0172<br>
    web: www.panemasters.ca
  </address>

  <div class="brand-name"><span class="mark"></span>PANE MASTERS</div>

  <h1 class="catalog-title">
    <span class="line-product">PRODUCT</span>
    <span class="line-catalog">CATALOG</span>
    <span class="line-year">2019</span>
  </h1>
</main>
</body>
</html>
```